international life style business needs a App Design

We need a App design for an application that will help people find fashion items that the don't know the name of or don't know where to buy. We would like to see designs that is neat and clear. People will be able to search certain pictures and post pictures also searching by name will bring a list of results. The final design should give people the option to find and show their own fashion idea

Industry/Entity Type

Fashion

Font styles to use
Serif

Requirements
Must have
• a search page and a result page also the option to upload pictures. Personal profile where pics and images searched stand out. Photo making option.Roadmap -→ easy to follow for users.
• The roadmap trough the app has to have the following things.
• 1. Introduction app.
• 2. Login/ registration. Also possible to connect trough loomtree or vividrift.
• 3. A personal profile page where pictures and images can be uploaded and shows searched images. Also the amount of following persons most be shown in the personal page.
• 4. A search page where in the top of the page there is a search option and below that images shown of items the person may like.
• 5. Result page that shows multiple images.

```html
<!DOCTYPE html>
<html lang="en">
<head>
<meta charset="utf-8">
<title>My Profile</title>
<link href="https://fonts.googleapis.com/css2?family=Roboto:wght@300;400;500&display=swap" rel="stylesheet">
<style>
  :root {
    --teal: #3cc2c4;
    --teal-light: #62d0d1;
    --page: #f3f3f3;
    --card: #ffffff;
    --ink: #333333;
    --muted: #9a9a9a;
    --line: #e6e6e6;
    --badge: #f7a0a0;
    --icon: #b9b9b9;
    --white: #ffffff;
  }
  * { margin: 0; padding: 0; box-sizing: border-box; }
  html, body { width: 805px; height: 1200px; overflow: hidden; background: var(--page); }
  body { font-family: "Roboto", Arial, sans-serif; color: var(--ink); }
  .screen { position: relative; width: 805px; height: 1200px; overflow: hidden; background: var(--page); }

  .topbar {
    position: absolute; left: 0; top: 0; width: 805px; height: 128px;
    background: linear-gradient(115deg, var(--teal) 0%, var(--teal) 62%, var(--teal-light) 62%, var(--teal-light) 100%);
    color: var(--white);
  }
  .status { position: absolute; top: 10px; left: 22px; right: 22px; height: 30px; display: flex; justify-content: space-between; align-items: center; font-size: 22px; font-weight: 400; }
  .status .carrier, .status .power { display: flex; align-items: center; gap: 8px; }
  .status .time { position: absolute; left: 50%; transform: translateX(-50%); }
  .header { position: absolute; top: 58px; left: 0; width: 100%; height: 50px; }
  .header .title { position: absolute; width: 100%; text-align: center; top: 6px; font-size: 30px; font-weight: 300; }
  .header .back { position: absolute; left: 62px; top: 2px; }
  .header .search { position: absolute; right: 52px; top: 2px; }

  .hero {
    position: absolute; left: 0; top: 128px; width: 805px; height: 377px;
    background: linear-gradient(180deg, #b9c4d0 0%, #e9c7bd 30%, #9fc3d2 48%, #5fa3bf 75%, #7bb7cc 100%);
    color: var(--white);
  }
  .hero .stat { position: absolute; top: 100px; width: 160px; text-align: center; }
  .hero .stat .label { font-size: 22px; font-weight: 300; opacity: .85; }
  .hero .stat .value { font-size: 32px; font-weight: 300; margin-top: 6px; }
  .stat.age { left: 52px; }
  .stat.followers { left: 573px; }
  .avatar {
    position: absolute; left: 290px; top: 33px; width: 208px; height: 208px; border-radius: 50%;
    border: 6px solid rgba(255,255,255,.9);
    background: radial-gradient(circle at 50% 40%, #d9a98c 0%, #a8735a 55%, #4d6a58 100%);
  }
  .profile-name { position: absolute; top: 255px; width: 100%; text-align: center; font-size: 36px; font-weight: 400; }
  .profile-city { position: absolute; top: 302px; width: 100%; text-align: center; font-size: 22px; font-weight: 300; }

  .item-card { position: absolute; width: 367px; height: 378px; background: var(--card); box-shadow: 0 1px 2px rgba(0,0,0,.06); }
  .card-1 { left: 23px; top: 533px; }
  .card-2 { left: 410px; top: 533px; }
  .card-3 { left: 23px; top: 932px; }
  .card-4 { left: 410px; top: 932px; }
  .price { position: absolute; left: 11px; top: 10px; width: 85px; height: 44px; background: var(--badge); color: var(--white); font-size: 20px; line-height: 44px; text-align: center; }
  .brand { position: absolute; left: 120px; top: 14px; font-size: 19px; font-weight: 400; color: var(--ink); }
  .product { position: absolute; left: 120px; top: 40px; font-size: 16px; font-weight: 300; color: var(--muted); }
  .visual { position: absolute; left: 70px; top: 84px; width: 227px; height: 222px; border-radius: 6px; }
  .visual.cardigan { background: linear-gradient(180deg, #2b3547, #1c2434); }
  .visual.tribal { left: 90px; width: 187px; top: 100px; height: 190px; background: linear-gradient(135deg, #2fa9b8, #d24f8c 50%, #2a2f57); }
  .visual.denim { left: 95px; top: 92px; width: 180px; background: linear-gradient(180deg, #d9e1e4, #b7c4cb); }
  .visual.plaid { left: 95px; top: 92px; width: 180px; background: linear-gradient(90deg, #e6a3c2, #6f7e96, #e6a3c2); }
  .card-footer { position: absolute; left: 17px; right: 17px; top: 330px; border-top: 1px solid var(--line); height: 48px; display: flex; align-items: center; justify-content: center; gap: 46px; font-size: 14px; color: var(--muted); }
  .card-footer span { display: flex; align-items: center; gap: 10px; }

  .tabbar { position: absolute; left: 0; top: 1099px; width: 805px; height: 101px; background: var(--white); border-top: 1px solid var(--line); z-index: 2; }
  .tabbar .divider { position: absolute; top: 18px; width: 1px; height: 58px; background: var(--line); }
  .tabbar .tab { position: absolute; top: 22px; }
</style>
</head>
<body>
<main class="screen">
  <header class="topbar">
    <div class="status">
      <div class="carrier">
        <svg width="70" height="14" viewBox="0 0 70 14"><g fill="#fff"><circle cx="7" cy="7" r="6"/><circle cx="21" cy="7" r="6"/><circle cx="35" cy="7" r="6"/></g><g fill="none" stroke="#fff" stroke-width="1.5"><circle cx="49" cy="7" r="5.2"/><circle cx="63" cy="7" r="5.2"/></g></svg>
        <span>VOLT</span>
        <svg width="22" height="16" viewBox="0 0 22 16" fill="none" stroke="#fff" stroke-width="2.2" stroke-linecap="round"><path d="M2 6a13 13 0 0 1 18 0"/><path d="M5.5 9.5a8 8 0 0 1 11 0"/><circle cx="11" cy="13.5" r="1.4" fill="#fff"/></svg>
      </div>
      <div class="time">4:21 PM</div>
      <div class="power">
        <svg width="12" height="22" viewBox="0 0 12 22" fill="none" stroke="#fff" stroke-width="1.6"><path d="M1 6l10 10-5 5V1l5 5L1 16"/></svg>
        <span>100%</span>
        <svg width="52" height="20" viewBox="0 0 52 20"><rect x="1" y="1" width="46" height="18" rx="3" fill="none" stroke="#fff" stroke-width="1.5"/><rect x="3.5" y="3.5" width="41" height="13" rx="1.5" fill="#fff"/><rect x="48.5" y="7" width="2.5" height="6" fill="#fff"/></svg>
      </div>
    </div>
    <div class="header">
      <svg class="back" width="26" height="46" viewBox="0 0 26 46" fill="none" stroke="#fff" stroke-width="2.2" stroke-linecap="round"><path d="M23 2L3 23l20 21"/></svg>
      <div class="title">My Profile</div>
      <svg class="search" width="48" height="48" viewBox="0 0 48 48" fill="none" stroke="#fff" stroke-width="2.4" stroke-linecap="round"><circle cx="20" cy="20" r="16"/><path d="M32 32l13 13"/></svg>
    </div>
  </header>

  <section class="hero" role="img" aria-label="Blurred photo of the sea at sunset behind the profile">
    <div class="stat age"><div class="label">Age</div><div class="value">22</div></div>
    <div class="stat followers"><div class="label">Followers</div><div class="value">586</div></div>
    <div class="avatar" role="img" aria-label="Profile photo of the user"></div>
    <div class="profile-name">Tessa Marlow</div>
    <div class="profile-city">San Francisco, CA</div>
  </section>

  <article class="item-card card-1">
    <div class="price">$6.99</div>
    <div class="brand">Norvik</div>
    <div class="product">Polka Cardigan Navy</div>
    <div class="visual cardigan" role="img" aria-label="Product photo of a navy polka dot cardigan"></div>
    <div class="card-footer">
      <span><svg width="24" height="22" viewBox="0 0 24 22" fill="none" stroke="#b9b9b9" stroke-width="1.5"><path d="M12 20S2 13.5 2 7.2A5 5 0 0 1 12 5a5 5 0 0 1 10 2.2C22 13.5 12 20 12 20z"/></svg>Like</span>
      <span><svg width="22" height="22" viewBox="0 0 22 22" fill="none" stroke="#b9b9b9" stroke-width="1.4"><circle cx="11" cy="11" r="9"/><path d="M2 11h18M11 2c3 3 3 15 0 18M11 2c-3 3-3 15 0 18"/></svg>Go to Website</span>
    </div>
  </article>

  <article class="item-card card-2">
    <div class="price">$9.99</div>
    <div class="brand">Juniper Lane</div>
    <div class="product">Tribal Aztec top</div>
    <div class="visual tribal" role="img" aria-label="Product photo of a patterned tribal crop top"></div>
    <div class="card-footer">
      <span><svg width="24" height="22" viewBox="0 0 24 22" fill="none" stroke="#b9b9b9" stroke-width="1.5"><path d="M12 20S2 13.5 2 7.2A5 5 0 0 1 12 5a5 5 0 0 1 10 2.2C22 13.5 12 20 12 20z"/></svg>Like</span>
      <span><svg width="22" height="22" viewBox="0 0 22 22" fill="none" stroke="#b9b9b9" stroke-width="1.4"><circle cx="11" cy="11" r="9"/><path d="M2 11h18M11 2c3 3 3 15 0 18M11 2c-3 3-3 15 0 18"/></svg>Go to Website</span>
    </div>
  </article>

  <article class="item-card card-3">
    <div class="price">$8.99</div>
    <div class="brand">Harbor &amp; Pine</div>
    <div class="product">Marylin Jeans cut</div>
    <div class="visual denim" role="img" aria-label="Product photo of a light checked shirt"></div>
  </article>

  <article class="item-card card-4">
    <div class="brand">Northfield Supply</div>
    <div class="product">Jester Plaid shorts</div>
    <div class="visual plaid" role="img" aria-label="Product photo of pink plaid shorts"></div>
  </article>

  <nav class="tabbar">
    <svg class="tab" style="left:100px" width="56" height="52" viewBox="0 0 56 52" fill="none" stroke="#b9b9b9" stroke-width="2" stroke-linecap="round"><path d="M28 36V4M16 15L28 3l12 12"/><path d="M3 30v19h50V30"/></svg>
    <div class="divider" style="left:277px"></div>
    <svg class="tab" style="left:363px" width="76" height="56" viewBox="0 0 76 56" fill="none" stroke="#b9b9b9" stroke-width="2"><rect x="2" y="10" width="72" height="44" rx="6"/><path d="M22 10l5-8h22l5 8"/><circle cx="38" cy="32" r="15"/><circle cx="38" cy="32" r="9"/></svg>
    <div class="divider" style="left:525px"></div>
    <svg class="tab" style="left:638px" width="56" height="56" viewBox="0 0 56 56" fill="none" stroke="#b9b9b9" stroke-width="2" stroke-linecap="round"><circle cx="23" cy="23" r="19"/><path d="M37 37l16 16"/></svg>
  </nav>
</main>
</body>
</html>
```